Need simple and modern looking business card with all my information on one side and logo on the other side
Info :
Company name - VELMAR CONSTRUCTION LLC
Company addres- 418 harbor 87th. Dunmoor park ny 10352
Email- velmarllc@tridomail.Com
Company phone number 555-318-6094
Cell number- 555-742-0583
Web site - velmarllc.Com
My name Gerald tomasino

Target Market(s)

Construction , home improvement, remodeling

Industry/Entity Type

Construction

Contact Information for Business Card

It has to be moder but at the same time simple

Font styles to use
Sans Serif

Colors
0255a3
ffffff
000000
f78f20
b1b1b1
9d9d9d
1b1b1b
33a6d7
ec1f27

Requirements
Must have
• My logo on one side maybe with a some kind of background on the other side all my information
Nice to have
• Some kind of background pictures provided by you .PLEASE HAVE ACCOUNT WITH PIXELVAULT WILL NOT PAY ANY EXTRA FEES .
Should not have
• Any kind of hamer, nails,screws, helmets itp. Please do not copy the other designs come up with something new.

```html
<!DOCTYPE html>
<html lang="en">
<head>
<meta charset="utf-8">
<title>Velmar Construction LLC – Business Card</title>
<link rel="stylesheet" href="https://fonts.googleapis.com/css2?family=Source+Sans+3:wght@400;600;700&display=swap">
<style>
  :root {
    --stage: #141414;
    --paper: #ffffff;
    --orange: #f7941d;
    --ink: #111111;
    --white: #ffffff;
  }
  * { margin: 0; padding: 0; box-sizing: border-box; }
  html, body {
    width: 1200px;
    height: 900px;
    overflow: hidden;
    background: var(--stage);
    font-family: "Source Sans 3", sans-serif;
  }
  .stage {
    position: relative;
    width: 1200px;
    height: 900px;
  }
  .card {
    position: absolute;
    top: 170px;
    width: 347px;
    height: 561px;
  }
  .card--front {
    left: 259px;
    background: var(--paper);
    text-align: center;
    color: var(--ink);
  }
  .card--back {
    left: 631px;
    background: var(--orange);
  }
  .tab {
    position: absolute;
    left: 102px;
    width: 143px;
    background: var(--orange);
  }
  .tab--top { top: 0; height: 30px; }
  .tab--bottom { bottom: 0; height: 28px; }

  .wordmark {
    position: absolute;
    font-weight: 600;
    line-height: 1;
  }
  .wordmark__name { display: block; letter-spacing: 0.02em; }
  .wordmark__tag { display: block; letter-spacing: 0.08em; }

  .card--front .wordmark {
    top: 88px;
    left: 0;
    width: 100%;
    color: var(--ink);
  }
  .card--front .wordmark__name { font-size: 52px; }
  .card--front .wordmark__tag { font-size: 18px; margin-top: 4px; }

  .card--back .wordmark {
    right: 56px;
    top: 424px;
    text-align: right;
    color: var(--white);
  }
  .card--back .wordmark__name { font-size: 48px; }
  .card--back .wordmark__tag { font-size: 16px; margin-top: 3px; }

  .holder {
    position: absolute;
    top: 221px;
    left: 0;
    width: 100%;
    font-size: 22px;
    font-weight: 700;
    color: var(--orange);
  }
  .contact {
    position: absolute;
    left: 0;
    width: 100%;
    font-size: 15px;
    line-height: 20px;
    font-style: normal;
  }
  .contact--phone { top: 300px; }
  .contact--address { top: 388px; }
  .website {
    position: absolute;
    top: 475px;
    left: 0;
    width: 100%;
    font-size: 15px;
    color: var(--orange);
  }
</style>
</head>
<body>
  <main class="stage">
    <section class="card card--front" aria-label="Business card front">
      <div class="tab tab--top"></div>
      <h1 class="wordmark">
        <span class="wordmark__name">VELMAR</span>
        <span class="wordmark__tag">CONSTRUCTION LLC</span>
      </h1>
      <p class="holder">Gerald tomasino</p>
      <address class="contact contact--phone">
        555-318-6094<br>
        555-742-0583<br>
        velmarllc@tridomail.Com
      </address>
      <address class="contact contact--address">
        418 harbor 87th.<br>
        Dunmoor park ny 10352
      </address>
      <p class="website">www.velmarllc.com</p>
      <div class="tab tab--bottom"></div>
    </section>

    <section class="card card--back" aria-label="Business card back">
      <p class="wordmark">
        <span class="wordmark__name">VELMAR</span>
        <span class="wordmark__tag">CONSTRUCTION LLC</span>
      </p>
    </section>
  </main>
</body>
</html>
```